business card, letterhead, email signature, post card, ect...
RIDER HOLDS FAST / DREAM - BELIEVE - ACT
Thank you so much designers!
Please do not submitted any more drafts. I have many great looking one. enough for me to choose one. I will make the decision with few other people to pick the right one no later than this Saturday.
Again thank you so much!
K48302977
Hi Designers,
Thank you so much for all the beautiful job. There are so many great looking cards. It will take me a little more time to ask others to help me pick the right one. I will make my decision no later than Saturday.
Again thank you so very much! I wish can have all of them but that is not how it works. Someone have to win.
Thank you all!
Hi designers,
Thank you so much, you are so very talented. I have a lot to look thru and decide which one to choose and work with. This is a very difficult job for me. I will let you know very, very soon. I don't have time to put the stars because there are too many of them.
Thank you, thank you and good luck to all of you!
TR/KWH/JP Team
Hi Plumo,
you got all the attention from me now, that is good.
Let work on #18:
1- take the fax out from everything
2- put the word "DREAM BELIEVE ACT" under every RHF logo except for the business card because the back of the card already have that word.
3- The letterhead and envelop have to much black. My suggestion is maybe you change the logo to black and a few lines of black, red or grey to accomplished that.
4- can you name each item so I know what it is.
Thanks and have a nice day!
please upload Ai file of your logo

```html
<!DOCTYPE html>
<html lang="en">
<head>
<meta charset="utf-8">
<title>Rider Holds Fast – Business Card</title>
<link rel="stylesheet" href="https://fonts.googleapis.com/css2?family=Roboto+Condensed:wght@400;700;800&display=swap">
<style>
  :root {
    --ink: #0b0b0b;
    --red: #e3202a;
    --red-deep: #b8141c;
    --white: #ffffff;
    --stage: #e9e9ea;
    --muted: #cfcfcf;
  }
  * { box-sizing: border-box; margin: 0; padding: 0; }
  html, body {
    width: 1200px; height: 980px; overflow: hidden;
    background: var(--stage);
    font-family: "Roboto Condensed", Arial, sans-serif;
  }
  .sheet {
    width: 1200px; height: 980px;
    display: flex; flex-direction: column;
    align-items: center; justify-content: center; gap: 30px;
  }
  .card {
    position: relative;
    width: 800px; height: 457px;
    border-radius: 26px;
    overflow: hidden;
    background: var(--ink);
    box-shadow: 0 6px 18px rgba(0,0,0,.18);
  }
  .card-art { position: absolute; inset: 0; }

  /* front */
  .brand {
    position: absolute; left: 130px; top: 120px;
    color: var(--white); font-weight: 800;
  }
  .brand-initials { font-size: 92px; line-height: .9; letter-spacing: 2px; }
  .brand-name { font-size: 17px; letter-spacing: 3px; margin-top: 4px; }
  .contact {
    position: absolute; left: 44px; top: 268px;
    list-style: none; color: var(--muted);
    font-size: 15px; line-height: 22px;
  }
  .contact li { display: flex; align-items: center; gap: 9px; }
  .contact-dot {
    width: 9px; height: 9px; border-radius: 50%;
    background: var(--red); flex: none;
  }
  .holder {
    position: absolute; right: 40px; bottom: 38px;
    text-align: right; color: var(--ink);
  }
  .holder-name { font-size: 28px; font-weight: 700; }
  .holder-role { font-size: 20px; }

  /* back */
  .site {
    position: absolute; left: 50%; top: 50%;
    transform: translate(-50%, -50%);
    display: flex; align-items: center; gap: 18px;
    font-size: 38px; font-weight: 700; color: var(--white);
    letter-spacing: 1px;
  }
  .site-mark {
    width: 34px; height: 34px; border-radius: 50%;
    background: var(--red); flex: none;
  }
  .site-name { color: var(--red); }
</style>
</head>
<body>
<main class="sheet">

  <section class="card card-front" aria-label="Business card front">
    <svg class="card-art" viewBox="0 0 800 457" aria-hidden="true">
      <path d="M0 0 H800 V457 H370 C620 120 300 -20 0 100 Z" fill="var(--red)"/>
      <path d="M0 100 C300 -20 620 120 370 457 H346 C590 130 300 10 0 122 Z" fill="var(--white)"/>
      <path d="M0 122 C300 10 590 130 346 457 H334 C575 140 300 25 0 134 Z" fill="var(--ink)"/>
      <path d="M0 0 H200 C120 18 50 45 0 70 Z" fill="var(--red-deep)"/>
    </svg>

    <div class="brand">
      <div class="brand-initials">RHF</div>
      <div class="brand-name">RIDER HOLDS FAST</div>
    </div>

    <ul class="contact">
      <li><span class="contact-dot"></span>1450 Harbor Rd, Ste 12</li>
      <li><span class="contact-dot"></span>Lakeview, OR 97630</li>
      <li><span class="contact-dot"></span>T (555) 201-4478</li>
      <li><span class="contact-dot"></span>M (555) 201-4479</li>
      <li><span class="contact-dot"></span>info@riderholdsfast.com</li>
      <li><span class="contact-dot"></span>www.riderholdsfast.com</li>
    </ul>

    <div class="holder">
      <div class="holder-name">Marcus Vale</div>
      <div class="holder-role">Founder / CEO</div>
    </div>
  </section>

  <section class="card card-back" aria-label="Business card back">
    <div class="site">
      <span class="site-mark"></span>
      <span>www.<span class="site-name">RiderHoldsFast</span>.com</span>
    </div>
  </section>

</main>
</body>
</html>
```